Cedar Ridge Planting Works and Sun-Sprout Megamart

The billboard will be on highway frontage and located directly next to my business building the marketing is for. The marketing on the billboard will be more directed towards the sun-sprouts megamart service being provided. And since the sign is on the businesses property it will need to say, "Exit Right Now" along with an arrow pointing to the right when facing the sign.

```html
<!DOCTYPE html>
<html lang="en">
<head>
<meta charset="utf-8">
<title>Cedar Ridge Planting Works – Highway Billboard</title>
<link href="https://fonts.googleapis.com/css2?family=Archivo+Black&family=Oswald:wght@500&display=swap" rel="stylesheet">
<style>
  :root {
    --page-bg: #e6e8eb;
    --board-black: #1c1a1d;
    --brand-green: #7dbb2e;
    --accent-orange: #f39419;
    --frame-lime: #b5d65a;
    --cta-white: #ffffff;
    --burger-brown: #8a5a36;
    --burger-dark: #3a2a24;
    --sprout-purple: #6b3f7a;
    --juice-wood: #5c4330;
    --juice-green: #4f8a2a;
    --farm-light: #e9edf2;
    --farm-green: #7fb352;
  }
  * { margin: 0; padding: 0; box-sizing: border-box; }
  html, body { width: 1200px; height: 1086px; overflow: hidden; background: var(--page-bg); }
  .billboard {
    position: absolute; left: 0; top: 368px;
    width: 1200px; height: 350px;
    background: var(--board-black);
    overflow: hidden;
  }
  .hero-photo {
    position: absolute; left: 0; top: 0; width: 420px; height: 350px;
    background:
      radial-gradient(ellipse 150px 120px at 140px 180px, #c7834a 0%, var(--burger-brown) 45%, transparent 75%),
      radial-gradient(ellipse 140px 110px at 290px 80px, var(--sprout-purple) 0%, transparent 70%),
      linear-gradient(90deg, var(--burger-dark) 0%, #4a3530 60%, var(--board-black) 100%);
  }
  .brand-name {
    position: absolute; left: 446px; top: 52px; width: 290px;
    display: flex; align-items: center; gap: 12px;
    font-family: "Oswald", sans-serif; font-weight: 500;
    font-size: 40px; line-height: 1.05; color: var(--brand-green);
  }
  .brand-dot {
    flex: none; width: 22px; height: 22px; border-radius: 50%;
    background: var(--brand-green);
  }
  .feature-photo {
    position: absolute; top: 29px; width: 181px; height: 149px;
    border: 6px solid;
  }
  .feature-photo--juice {
    left: 777px; border-color: var(--accent-orange);
    background: radial-gradient(circle at 55% 55%, var(--juice-green) 0 18%, transparent 20%),
                linear-gradient(160deg, #a58a68 0%, var(--juice-wood) 55%, #2e231b 100%);
  }
  .feature-photo--farm {
    left: 992px; border-color: var(--frame-lime);
    background: linear-gradient(180deg, var(--farm-light) 0%, #c9ced6 50%, var(--farm-green) 75%, #4d8a33 100%);
  }
  .cta {
    position: absolute; left: 452px; top: 208px;
    font-family: "Archivo Black", sans-serif;
    font-size: 71px; line-height: 1; letter-spacing: 0.5px;
    color: var(--cta-white);
  }
  .cta-arrow { position: absolute; left: 1064px; top: 216px; width: 110px; height: 74px; }
  .brush-band { position: absolute; left: 0; bottom: 0; width: 1200px; height: 46px; }
</style>
</head>
<body>
  <section class="billboard">
    <div class="hero-photo" role="img" aria-label="Photo of a chicken burger with red onion, lettuce, tomato and micro-greens on a plate"></div>

    <div class="brand-name"><span class="brand-dot"></span><span>Cedar Ridge Planting Works</span></div>

    <div class="feature-photo feature-photo--juice" role="img" aria-label="Photo of a glass of green wheatgrass juice on a wooden board"></div>
    <div class="feature-photo feature-photo--farm" role="img" aria-label="Photo of an indoor vertical farm with grow lights over rows of greens"></div>

    <p class="cta">Exit Right Now</p>
    <svg class="cta-arrow" viewBox="0 0 110 74" aria-hidden="true">
      <polygon points="0,22 66,22 66,0 110,37 66,74 66,52 0,52" fill="var(--accent-orange)"/>
    </svg>

    <svg class="brush-band" viewBox="0 0 1200 46" preserveAspectRatio="none" aria-hidden="true">
      <path fill="var(--accent-orange)" d="M0,22 L40,18 L90,21 L150,14 L210,19 L260,12 L330,17 L400,10 L470,15 L530,8 L600,13 L660,6 L720,11 L790,4 L850,9 L910,3 L980,8 L1040,2 L1100,7 L1160,1 L1200,4 L1200,46 L0,46 Z"/>
      <path fill="var(--accent-orange)" d="M300,6 L340,4 L335,8 Z M560,2 L610,1 L600,5 Z M880,0 L930,0 L915,3 Z"/>
    </svg>
  </section>
</body>
</html>
```